Bright Oak Fitness Facility Business Cards

Business Card Design that incorporates the logo and tagline

Target Market(s)

Fitness, People Who Exercise

Contact Information for Business Card

2817 Mossgrove Bend Road
Tavares, Florida 32190
Phone: 352-555-Jump (5867)
www.brightoakfitness.example
info@brightoakfitness.example

Requirements
Must have
• Logo, Address, Website, email and tagline "More Than A Gym". Colors should be red/black/grey/white

```html
<!DOCTYPE html>
<html lang="en">
<head>
<meta charset="utf-8">
<title>Bright Oak Fitness – Business Card</title>
<link rel="stylesheet" href="https://fonts.googleapis.com/css2?family=Barlow:wght@400;600;700;800&display=swap">
<style>
  :root {
    --brand-red: #ed1c24;
    --ink-black: #000000;
    --text-dark: #1a1a1a;
    --card-white: #ffffff;
    --frame-grey: #333333;
  }
  html, body {
    margin: 0;
    padding: 0;
    width: 1200px;
    height: 1000px;
    overflow: hidden;
    background: var(--card-white);
  }
  .business-card {
    display: block;
    width: 1200px;
    height: 1000px;
  }
  .card-frame { fill: var(--card-white); stroke: var(--frame-grey); stroke-width: 1.2; }
  .tagline { font-family: "Barlow", sans-serif; font-weight: 800; font-size: 136px; }
  .tagline-top { fill: var(--brand-red); }
  .tagline-bottom { fill: var(--ink-black); }
  .rule-red { fill: var(--brand-red); }
  .rule-black { fill: var(--ink-black); }
  .contact { font-family: "Barlow", sans-serif; font-size: 27px; fill: var(--text-dark); letter-spacing: 0.5px; }
  .contact-label { font-weight: 700; fill: var(--ink-black); }
  .contact-web { font-weight: 700; fill: var(--ink-black); }
  .web-underline { fill: var(--ink-black); }
  .brand-mark { fill: var(--brand-red); }
  .brand-name { font-family: "Barlow", sans-serif; font-weight: 700; font-size: 32px; fill: var(--ink-black); }
</style>
</head>
<body>
<svg class="business-card" viewBox="0 0 1200 1000" xmlns="http://www.w3.org/2000/svg">
  <rect class="card-frame" x="96" y="211" width="1008" height="578"/>

  <g class="tagline-block">
    <text class="tagline tagline-top" x="134" y="338" textLength="746" lengthAdjust="spacingAndGlyphs">MORE THAN</text>
    <rect class="rule-red" x="134" y="346" width="746" height="14"/>
    <text class="tagline tagline-bottom" x="125" y="468" textLength="394" lengthAdjust="spacingAndGlyphs">A GYM</text>
    <rect class="rule-black" x="125" y="475" width="394" height="15"/>
  </g>

  <g class="contact-block">
    <text class="contact" x="126" y="593">2817 Mossgrove Bend Road</text>
    <text class="contact" x="126" y="632">Tavares, Florida 32190</text>
    <text class="contact" x="126" y="671"><tspan class="contact-label">P /</tspan> 352-555-Jump (5867)</text>
    <text class="contact" x="126" y="710"><tspan class="contact-label">E /</tspan> info@brightoakfitness.example</text>
    <text class="contact contact-web" x="126" y="748" textLength="389" lengthAdjust="spacingAndGlyphs">www.brightoakfitness.example</text>
    <rect class="web-underline" x="126" y="752" width="389" height="3"/>
  </g>

  <g class="brand-lockup">
    <rect class="brand-mark" x="893" y="622" width="44" height="44"/>
    <text class="brand-name" x="765" y="728" textLength="300" lengthAdjust="spacingAndGlyphs">BRIGHT OAK FITNESS</text>
  </g>
</svg>
</body>
</html>
```